Fund Harbor

We need desigin for our main page(concept will be used for other pages also).
We already have a logo, and moqup of our main page(see attch).
You could change layers and positions on moqup, but please use logo, and its colors in design creating. (We have logo in different colors, i attached 2 samples, so you could use also another colors if you wish).

Our bussinees will be something similar to LaunchPeak or Backwise.co, but with some special features. So main idea: start-ups, donations, investemnets

Designs were prefer:
http://backwise.co/
http://www.launchpeak.com/

Target Market(s)

Clients are middle aged persons, who interested in new start-ups, investments and so on.

Requirements
Must have
• Design must be neat

```html
<!DOCTYPE html>
<html lang="en">
<head>
<meta charset="utf-8">
<title>Fund Harbor</title>
<link rel="stylesheet" href="https://fonts.googleapis.com/css2?family=Arimo:wght@400;700&display=swap">
<style>
:root{
  --page:#a8a9ad;
  --page-light:#cfd0d3;
  --dark:#434144;
  --darker:#2a2a2c;
  --red:#e8212b;
  --red-soft:#f25a62;
  --white:#ffffff;
  --line:#d8d8d8;
  --text:#3b3b3b;
  --muted:#6a6a6a;
  --btn:#c9c9c9;
}
*{box-sizing:border-box;margin:0;padding:0}
html,body{width:1042px;height:1200px;overflow:hidden}
body{
  font-family:"Arimo",Arial,sans-serif;color:var(--text);
  background:radial-gradient(ellipse at 50% 45%,var(--page-light) 0%,var(--page) 70%);
  position:relative;
}
.abs{position:absolute}
/* header */
.brand-box{left:124px;top:16px;width:212px;height:113px;background:linear-gradient(#f4f4f4,#d9d9da);border:1px solid #c4c4c4;display:flex;flex-direction:column;align-items:center;justify-content:center;gap:6px}
.brand-dot{width:30px;height:30px;border-radius:50%;background:var(--red)}
.brand-name{font-size:25px;font-weight:700;color:var(--dark);letter-spacing:-.5px}
.main-nav{left:352px;top:16px;width:556px;height:78px;background:var(--white);display:flex;align-items:center;font-size:15px}
.main-nav a{color:var(--text);text-decoration:none;margin-left:15px;margin-right:16px}
.main-nav .active{background:var(--red);color:var(--white);font-weight:700;height:100%;width:122px;display:flex;align-items:center;justify-content:center;margin:0}
.search-bar{left:352px;top:106px;width:556px;height:23px;background:var(--white);border:1px solid #cfcfcf}
.search-field{left:141px;top:2px;width:267px;height:17px;border:1px solid #cfcfcf;font-size:11px;padding:2px 5px;color:var(--muted)}
.search-btn{left:408px;top:2px;width:19px;height:17px;background:var(--red)}
.lang{left:433px;top:2px;width:119px;height:17px;border:1px solid #cfcfcf;font-size:11px;padding:2px 4px}
.lang::after{content:"";position:absolute;right:3px;top:2px;width:11px;height:11px;border:1px solid #aaa;background:linear-gradient(#fff,#e4e4e4)}
/* stats */
.stats{left:124px;top:141px;width:178px;height:249px;background:var(--white);padding:8px 8px 0 6px;list-style:none}
.stats li{display:flex;align-items:center;height:24.5px;font-size:12.5px}
.stats li span{flex:1;border-bottom:1px solid #777;height:100%;display:flex;align-items:center;padding-left:4px;margin-left:8px}
.tick{width:15px;height:15px;flex:none}
/* video */
.video{left:310px;top:141px;width:412px;height:249px;background:radial-gradient(ellipse at 50% 40%,#fafafa,#cfcfd0);}
.video-name{left:0;width:412px;top:115px;text-align:center;font-size:40px;font-weight:700;color:var(--dark)}
.video-dot{left:186px;top:55px;width:40px;height:40px;border-radius:50%;background:var(--red)}
.controls{left:0;top:221px;width:412px;height:28px;background:linear-gradient(#3a3a3a,#161616);color:#999;font-size:9px}
.seek{left:0;top:-3px;width:412px;height:4px;background:#555}
.seek i{position:absolute;left:0;top:0;width:215px;height:4px;background:var(--red)}
.seek b{position:absolute;left:210px;top:-3px;width:10px;height:10px;border-radius:50%;background:#ddd}
/* login */
.login{left:729px;top:141px;width:179px;height:249px;background:var(--dark);color:var(--white)}
.login-tabs{display:flex;height:32px;font-size:13px}
.login-tabs div{flex:1;display:flex;align-items:center;justify-content:center}
.login-tabs .off{background:var(--white);color:var(--text);margin-left:4px}
.login label{position:absolute;left:14px;font-size:12.5px}
.login .field{position:absolute;left:14px;width:150px;height:18px;background:var(--white);border:1px solid #bbb}
.forgot{left:14px;top:145px;font-size:9px;color:var(--red);text-decoration:underline}
.btn{background:linear-gradient(#f2f2f2,#bdbdbd);color:var(--dark);font-weight:700;display:flex;align-items:center;justify-content:center}
.login .btn{position:absolute;left:14px;top:169px;width:83px;height:21px;font-size:13px}
.safe{left:14px;top:221px;font-size:10px;display:flex;gap:5px;align-items:center}
.safe i{width:9px;height:9px;background:var(--white);border:1px solid #999;display:block}
/* tabs */
.tab{top:402px;width:189px;height:43px;background:var(--white);border:1px solid #ddd;display:flex;align-items:center;justify-content:center;font-size:13px;color:var(--text)}
.tab.on{background:var(--dark);color:var(--white);border-color:var(--dark)}
/* cards */
.card{top:454px;width:189px;height:302px;background:var(--white);border:1px solid #ddd;text-align:center}
.card.on{background:var(--dark);border-color:var(--dark);color:var(--white)}
.card h3{font-size:22px;margin-top:20px;color:#444}
.card.on h3{color:var(--white)}
.thumb{position:absolute;left:10px;top:56px;width:168px;height:93px;background:linear-gradient(135deg,#c9c4a8,#8d8f78 50%,#c2c0aa);border:2px solid #e6e6e6}
.desc{position:absolute;left:10px;top:157px;width:170px;text-align:left;font-size:9.5px;line-height:12px;color:var(--muted)}
.card.on .desc{color:#eee}
.bar{position:absolute;left:10px;top:195px;width:168px;height:18px;background:var(--white);border:1px solid #999;font-size:9px;font-weight:700;color:#222;text-align:right;padding:3px 5px}
.bar i{position:absolute;left:1px;top:1px;height:14px;background:linear-gradient(var(--red-soft),var(--red))}
.bar span{position:relative}
.chip{position:absolute;height:17px;font-size:9px;font-weight:700;display:flex;align-items:center;justify-content:center;background:var(--btn);color:#444}
.card.on .chip{background:var(--white);color:#111}
.card .btn{position:absolute;left:52px;top:272px;width:83px;height:21px;font-size:13px}
/* view all */
.view-all{left:124px;top:765px;width:785px;height:99px;background:var(--dark);color:var(--white);text-align:center}
.view-all h2{font-size:20px;margin-top:14px}
.view-all p{font-size:10.5px;margin-top:2px}
.view-all .btn{width:83px;height:21px;margin:11px auto 0;font-size:12px}
/* connect */
.connect{left:124px;top:872px;width:785px;height:265px;background:var(--dark);color:var(--white);text-align:center}
.connect h2{font-size:17px;margin-top:25px}
.connect .sub{font-size:14px;margin-top:4px}
.social{position:absolute;top:86px;width:150px;font-size:7.5px;line-height:12px}
.social .ring{width:72px;height:72px;border-radius:50%;background:var(--white);margin:0 auto}
.social .name{font-size:14px;font-weight:700;margin-top:7px}
.social p{height:50px;margin-bottom:0}
.copyright{left:0;width:1042px;top:1152px;text-align:center;font-size:9.5px;color:#111}
</style>
</head>
<body>

<div class="abs brand-box"><div class="brand-dot"></div><div class="brand-name">Fund Harbor</div></div>

<nav class="abs main-nav">
  <a class="active" href="#">How it works?</a>
  <a href="#">Projects Review</a>
  <a href="#">Virtual Office</a>
</nav>

<div class="abs search-bar">
  <div class="abs search-field">search</div>
  <div class="abs search-btn">
    <svg width="19" height="17" viewBox="0 0 19 17"><circle cx="10.5" cy="7" r="3.5" fill="none" stroke="#fff" stroke-width="1.6"/><line x1="8" y1="9.5" x2="5" y2="13" stroke="#fff" stroke-width="2"/></svg>
  </div>
  <div class="abs lang">English</div>
</div>

<ul class="abs stats">
  <li><svg class="tick" viewBox="0 0 16 16"><circle cx="8" cy="8" r="8" fill="#444"/><path d="M4.5 8.2l2.3 2.3 4.7-4.8" fill="none" stroke="#fff" stroke-width="1.8"/></svg><span>$50 000 of investments</span></li>
  <li><svg class="tick" viewBox="0 0 16 16"><circle cx="8" cy="8" r="8" fill="#444"/><path d="M4.5 8.2l2.3 2.3 4.7-4.8" fill="none" stroke="#fff" stroke-width="1.8"/></svg><span>1600 start-ups</span></li>
  <li><svg class="tick" viewBox="0 0 16 16"><circle cx="8" cy="8" r="8" fill="#444"/><path d="M4.5 8.2l2.3 2.3 4.7-4.8" fill="none" stroke="#fff" stroke-width="1.8"/></svg><span>700 organizations</span></li>
  <li><svg class="tick" viewBox="0 0 16 16"><circle cx="8" cy="8" r="8" fill="#444"/><path d="M4.5 8.2l2.3 2.3 4.7-4.8" fill="none" stroke="#fff" stroke-width="1.8"/></svg><span>10 000 investors</span></li>
  <li><svg class="tick" viewBox="0 0 16 16"><circle cx="8" cy="8" r="8" fill="#444"/><path d="M4.5 8.2l2.3 2.3 4.7-4.8" fill="none" stroke="#fff" stroke-width="1.8"/></svg><span>5000 employees</span></li>
  <li><svg class="tick" viewBox="0 0 16 16"><circle cx="8" cy="8" r="8" fill="#444"/><path d="M4.5 8.2l2.3 2.3 4.7-4.8" fill="none" stroke="#fff" stroke-width="1.8"/></svg><span>2000 partners</span></li>
  <li><svg class="tick" viewBox="0 0 16 16"><circle cx="8" cy="8" r="8" fill="#444"/><path d="M4.5 8.2l2.3 2.3 4.7-4.8" fill="none" stroke="#fff" stroke-width="1.8"/></svg><span>$ 10 000 000 of pro fit</span></li>
</ul>

<div class="abs video">
  <div class="abs video-dot"></div>
  <div class="abs video-name">Fund Harbor</div>
  <div class="abs controls">
    <div class="abs seek"><i></i><b></b></div>
    <svg class="abs" style="left:20px;top:8px" width="12" height="12"><rect x="2" y="1" width="3" height="10" fill="#aaa"/><rect x="7" y="1" width="3" height="10" fill="#aaa"/></svg>
    <svg class="abs" style="left:53px;top:8px" width="18" height="12"><path d="M1 4h3l4-3v10l-4-3H1z" fill="#aaa"/><path d="M11 3q3 3 0 6M13 1q5 5 0 10" fill="none" stroke="#aaa"/></svg>
    <div class="abs" style="left:78px;top:13px;width:38px;height:3px;background:#555"><div style="width:32px;height:3px;background:var(--red)"></div></div>
    <div class="abs" style="left:133px;top:9px">04:24 / 09:35</div>
    <div class="abs" style="left:360px;top:9px">360p</div>
    <svg class="abs" style="left:390px;top:7px" width="14" height="14"><path d="M1 5V1h4M9 1h4v4M13 9v4H9M5 13H1V9" fill="none" stroke="#aaa" stroke-width="1.3"/></svg>
  </div>
</div>

<div class="abs login">
  <div class="login-tabs"><div>Login</div><div class="off">Registration</div></div>
  <label style="top:58px">Email or Phone</label>
  <div class="field" style="top:80px"></div>
  <label style="top:103px">Password</label>
  <div class="field" style="top:124px"></div>
  <div class="abs forgot">Forget password?</div>
  <div class="btn">Login</div>
  <div class="abs safe"><i></i>Sate login</div>
</div>

<div class="abs tab on" style="left:124px">Recommended</div>
<div class="abs tab" style="left:322px">Popular</div>
<div class="abs tab" style="left:521px">Most invested</div>
<div class="abs tab" style="left:719px">New</div>

<article class="abs card on" style="left:124px">
  <h3>Project A</h3>
  <div class="thumb" role="img" aria-label="Photo of banknotes"></div>
  <p class="desc">Very intersting thing short description of the project.</p>
  <div class="bar"><i style="width:95px"></i><span>70% succe</span></div>
  <div class="chip" style="left:32px;top:223px;width:122px">$90 000 invested</div>
  <div class="chip" style="left:12px;top:247px;width:80px">200 Investors</div>
  <div class="chip" style="left:97px;top:247px;width:77px">23 days left</div>
  <div class="btn">Invest</div>
</article>
<article class="abs card" style="left:322px">
  <h3>Project B</h3>
  <div class="thumb" role="img" aria-label="Photo of banknotes"></div>
  <p class="desc">Very intersting thing short description of the project.</p>
  <div class="bar"><i style="width:78px"></i><span>50% succe</span></div>
  <div class="chip" style="left:32px;top:223px;width:122px">$90 000 invested</div>
  <div class="chip" style="left:12px;top:247px;width:80px">200 Investors</div>
  <div class="chip" style="left:97px;top:247px;width:77px">23 days left</div>
  <div class="btn">Invest</div>
</article>
<article class="abs card" style="left:521px">
  <h3>Project C</h3>
  <div class="thumb" role="img" aria-label="Photo of banknotes"></div>
  <p class="desc">Very intersting thing short description of the project.</p>
  <div class="bar"><i style="width:110px"></i><span>80% succe</span></div>
  <div class="chip" style="left:32px;top:223px;width:122px">$90 000 invested</div>
  <div class="chip" style="left:12px;top:247px;width:80px">200 Investors</div>
  <div class="chip" style="left:97px;top:247px;width:77px">23 days left</div>
  <div class="btn">Invest</div>
</article>
<article class="abs card" style="left:719px">
  <h3>Project D</h3>
  <div class="thumb" role="img" aria-label="Photo of banknotes"></div>
  <p class="desc">Very intersting thing short description of the project.</p>
  <div class="bar"><i style="width:38px"></i><span>40% succe</span></div>
  <div class="chip" style="left:32px;top:223px;width:122px">$90 000 invested</div>
  <div class="chip" style="left:12px;top:247px;width:80px">200 Investors</div>
  <div class="chip" style="left:97px;top:247px;width:77px">23 days left</div>
  <div class="btn">Invest</div>
</article>

<section class="abs view-all">
  <h2>View all Projects?</h2>
  <p>more then 1000 projects</p>
  <div class="btn">Yes</div>
</section>

<section class="abs connect">
  <h2>Want the latest industry news and Fund Harbor updates before we launch the platform?</h2>
  <div class="sub">Stay connected with us.</div>
  <div class="social" style="left:155px"><p>We're on Circleface<br>Visit us to see our daily updates</p><div class="ring"></div><div class="name">Circleface</div></div>
  <div class="social" style="left:316px"><p>Follow @FundHarbor for breaking<br>industry news and updates on our daily<br>deals as they happen.</p><div class="ring"></div><div class="name">Chirper</div></div>
  <div class="social" style="left:478px"><p>Join the discussion and start the debate<br>on ProNet, where you will be connected<br>to our investor network.</p><div class="ring"></div><div class="name">ProNet</div></div>
</section>

<div class="abs copyright">Copyright © 2013 Fund Harbor.</div>

</body>
</html>
```